Update cover page from corporate ppt template

We would like you to design a new cover page for our corporate presentation template

Attached you will find our existing template with the previous cover pages used in the past years.

As you can see, we have used transparency lines in different directions and also tried to develop a new design with mosaic/squares but we are not entirely satisfied (logo lost in the sky, ...)

You can reuse the same picture (mountain with the bridge, i.e not the one of the last cover page)

Feel free to come up with new ideas

```html
<!DOCTYPE html>
<html lang="en">
<head>
<meta charset="utf-8">
<title>Board of Directors – Cover</title>
<link rel="stylesheet" href="https://fonts.googleapis.com/css2?family=Cinzel:wght@400;600&family=Montserrat:wght@400&display=swap">
<style>
  :root {
    --paper: #ffffff;
    --accent-blue: #6f8fcb;
    --title-blue: #6a88c6;
    --ink-grey: #6e6e6e;
    --name-grey: #7a7a7a;
    --sky-top: #3f78c4;
    --sky-low: #bcd6ee;
    --rock: #8d7556;
    --slope: #5f7a3a;
    --sea: #2f9fb4;
    --sea-deep: #1f6fa8;
  }
  html, body {
    margin: 0;
    padding: 0;
    width: 1200px;
    height: 675px;
    overflow: hidden;
    background: var(--paper);
  }
  .cover {
    position: relative;
    width: 1200px;
    height: 675px;
    overflow: hidden;
    background: var(--paper);
  }
  .hero-photo {
    position: absolute;
    inset: 0 0 auto 0;
    height: 560px;
    background:
      linear-gradient(180deg, rgba(63,120,196,0) 0%, rgba(63,120,196,0) 100%),
      linear-gradient(168deg,
        var(--sky-top) 0%,
        var(--sky-low) 18%,
        var(--rock) 26%,
        var(--slope) 40%,
        #d9d3c4 50%,
        var(--sea) 60%,
        var(--sea-deep) 100%);
  }
  .base-curve {
    position: absolute;
    left: 0;
    top: 0;
    width: 1200px;
    height: 675px;
  }
  .company-name {
    position: absolute;
    left: 0;
    width: 650px;
    top: 555px;
    text-align: center;
    font-family: "Cinzel", serif;
    font-weight: 400;
    font-size: 56px;
    letter-spacing: 1px;
    color: var(--name-grey);
    line-height: 1;
  }
  .divider {
    position: absolute;
    left: 549px;
    top: 517px;
    width: 2px;
    height: 144px;
    background: var(--accent-blue);
  }
  .cover-title {
    position: absolute;
    left: 640px;
    top: 533px;
    margin: 0;
    font-family: "Cinzel", serif;
    font-weight: 600;
    font-size: 36px;
    line-height: 1;
    color: var(--title-blue);
    letter-spacing: 0.5px;
  }
  .cover-date {
    position: absolute;
    left: 640px;
    top: 603px;
    margin: 0;
    font-family: "Cinzel", serif;
    font-weight: 600;
    font-size: 36px;
    line-height: 1;
    color: var(--ink-grey);
    letter-spacing: 0.5px;
  }
  .slide-code {
    position: absolute;
    right: 6px;
    bottom: 4px;
    font-family: "Montserrat", sans-serif;
    font-size: 9px;
    color: #333;
  }
</style>
</head>
<body>
<main class="cover">
  <div class="hero-photo" role="img" aria-label="Coastal landscape: sandstone mountain range above a hillside town, white sandy beach with granite boulders and turquoise ocean under a blue sky"></div>

  <svg class="base-curve" viewBox="0 0 1200 675" aria-hidden="true">
    <path d="M0 537 Q600 400 1200 537 L1200 675 L0 675 Z" fill="var(--paper)"/>
    <path d="M162 519 Q600 446 1094 530 Q600 470 162 519 Z" fill="var(--accent-blue)"/>
  </svg>

  <div class="company-name">VANTORA</div>

  <div class="divider"></div>

  <h1 class="cover-title">Board of Directors</h1>
  <p class="cover-date">May 2024</p>

  <span class="slide-code">C63</span>
</main>
</body>
</html>
```